Corvett Tiling Solutions, QBCC 4870312, ABN 38204917586, Email corvetttiling@mailbox-demo.com,Mobile 04918365

Corvett Tiling Solutions, is the name of my wall and floor tiling company and the details above are needed on the business card. Im open to see what people come up with i really have no colour requirements or other design specs as long as its not too plain.

```html
<!DOCTYPE html>
<html lang="en">
<head>
<meta charset="utf-8">
<title>Corvett Tiling Solutions – Business Card</title>
<link rel="stylesheet" href="https://fonts.googleapis.com/css2?family=Open+Sans:wght@300;400;700&display=swap">
<style>
  :root {
    --stage: #e9e9e9;
    --card-dark: #1c1c1c;
    --card-dark-2: #3a3a3a;
    --card-light: #ffffff;
    --accent: #ee6a3a;
    --accent-deep: #e2453a;
    --ink: #2a2a2a;
    --ink-soft: #8a8a8a;
    --on-dark: #f2f2f2;
    --on-dark-soft: #cfcfcf;
    --tile-grey: #bdbdbd;
    --tile-grey-soft: #e6e6e6;
    --rule: #3a3a3a;
  }
  * { box-sizing: border-box; margin: 0; padding: 0; }
  html, body { width: 1200px; height: 800px; overflow: hidden; }
  body {
    background: var(--stage);
    font-family: "Open Sans", Arial, sans-serif;
    position: relative;
  }

  /* Back of card */
  .card-back {
    position: absolute;
    left: 110px; top: 130px;
    width: 330px; height: 540px;
    background: var(--card-dark);
    box-shadow: 0 10px 24px rgba(0,0,0,.25);
    overflow: hidden;
  }
  .card-back .tile-field {
    position: absolute; inset: 0;
    background: linear-gradient(160deg, var(--card-dark-2) 0%, var(--card-dark) 55%, #111 100%);
  }
  .card-back .brand {
    position: absolute;
    left: 250px; top: 230px;
    transform: rotate(90deg);
    transform-origin: left top;
    display: flex; align-items: center; gap: 16px;
    white-space: nowrap;
  }
  .card-back .brand-mark {
    width: 24px; height: 24px;
    background: var(--accent);
  }
  .card-back .brand-name {
    font-weight: 300;
    font-size: 48px;
    line-height: 1;
    color: var(--on-dark);
  }
  .card-back .brand-tagline {
    font-weight: 400;
    font-size: 15px;
    letter-spacing: 2px;
    color: var(--on-dark-soft);
    margin-top: 8px;
  }

  /* Front of card */
  .card-front {
    position: absolute;
    left: 500px; top: 217px;
    width: 600px; height: 366px;
    background: var(--card-light);
    box-shadow: 0 10px 24px rgba(0,0,0,.22);
    overflow: hidden;
  }
  .card-front .brand {
    position: absolute;
    left: 270px; top: 34px;
    display: flex; align-items: center; gap: 16px;
  }
  .card-front .brand-mark {
    width: 46px; height: 46px;
    background: var(--ink);
  }
  .card-front .brand-name {
    font-weight: 300;
    font-size: 40px;
    line-height: 1;
    color: var(--accent);
  }
  .card-front .brand-tagline {
    font-weight: 400;
    font-size: 15px;
    letter-spacing: 1px;
    color: var(--ink);
    margin-top: 6px;
  }
  .card-front .contact {
    position: absolute;
    left: 34px; top: 116px;
  }
  .contact .person-name {
    font-weight: 700;
    font-size: 15px;
    letter-spacing: .5px;
    color: var(--accent-deep);
    text-transform: uppercase;
  }
  .contact .person-role {
    font-size: 12px;
    color: var(--ink-soft);
    margin-bottom: 12px;
  }
  .contact .line {
    display: flex; align-items: center; gap: 10px;
    font-size: 13px; color: var(--ink);
    margin-bottom: 6px;
  }
  .contact .icon {
    width: 16px; height: 16px;
    background: var(--accent-deep);
    display: flex; align-items: center; justify-content: center;
  }
  .contact .credentials {
    font-size: 12px;
    color: var(--ink-soft);
    margin-top: 8px;
  }
  .card-front .tile-fade {
    position: absolute;
    right: 0; top: 190px;
    width: 280px; height: 90px;
    background: linear-gradient(90deg, rgba(230,230,230,0) 0%, var(--tile-grey-soft) 70%);
  }
  .card-front .divider {
    position: absolute;
    left: 0; right: 0; top: 284px;
    height: 1px; background: var(--rule);
  }
  .card-front .tile-band {
    position: absolute;
    left: 0; right: 0; bottom: 0;
    height: 76px;
    background: linear-gradient(180deg, var(--tile-grey) 0%, #7a7a7a 100%);
  }
</style>
</head>
<body>

  <section class="card-back" aria-label="Card back">
    <div class="tile-field" role="img" aria-label="Dark quilted diamond tile pattern"></div>
    <div class="brand">
      <span class="brand-mark"></span>
      <div>
        <p class="brand-name">Corvett</p>
        <p class="brand-tagline">TILING SOLUTIONS</p>
      </div>
    </div>
  </section>

  <section class="card-front" aria-label="Card front">
    <div class="brand">
      <span class="brand-mark"></span>
      <div>
        <p class="brand-name">Corvett</p>
        <p class="brand-tagline">TILING SOLUTIONS</p>
      </div>
    </div>

    <div class="contact">
      <p class="person-name">Dana Wrexford</p>
      <p class="person-role">Director</p>
      <p class="line">
        <span class="icon">
          <svg width="10" height="10" viewBox="0 0 10 10"><path d="M2 1 L4 1 L4.6 3 L3.5 3.8 Q4.5 5.8 6.2 6.5 L7 5.4 L9 6 L9 8 Q5 9 2.5 6.5 Q1 4.5 2 1 Z" fill="#fff"/></svg>
        </span>
        04918365
      </p>
      <p class="line">
        <span class="icon">
          <svg width="10" height="10" viewBox="0 0 10 10"><rect x="1" y="2.5" width="8" height="5.5" fill="none" stroke="#fff" stroke-width="1"/><path d="M1 2.5 L5 5.5 L9 2.5" fill="none" stroke="#fff" stroke-width="1"/></svg>
        </span>
        corvetttiling@mailbox-demo.com
      </p>
      <p class="credentials">QBCC 4870312 &nbsp;·&nbsp; ABN 38204917586</p>
    </div>

    <div class="tile-fade" role="img" aria-label="Faint grey stepped tile squares"></div>
    <div class="divider"></div>
    <div class="tile-band" role="img" aria-label="Grey diamond tile pattern band"></div>
  </section>

</body>
</html>
```